PLUM BUSINESS CARD

Need a business card and logo. The company name is PLUM (Coastal Society of Junior Equestrian Arts). It's a business that offers horseback riding lessons to young girls. Please put my name: Marlene Tobbitt and a place for email and phone number. I would like the card to look feminine and soft. I like script type lettering. I want the card to be white or ivory with black or gray and hot pink print. A horse head outline would be cool, something whimsical. Think teen girl who likes glamour. Also, I give western riding lessons. So I like faded out background Images of western saddles, cowgirls, horses with long hair, ropes, horses in sunset...mabe the word PLUM can be made out of a lasso rope?

Just updated my project with a little more detail

Target Market(s)

Young girls/ cowgirls, western riding

Industry/Entity Type

Horseback Riding

Font styles to use
Script

Colors
e34197

Requirements
Must have
• A logo of PLUM.
Must say Coastal Society of Junior Equestrian Arts
Colors are Pink and Black with an elegant, glamorous, feminine look.
Nice to have
• Could have a picture or outline of a horse

```html
<!DOCTYPE html>
<html lang="en">
<head>
<meta charset="utf-8">
<title>PLUM Business Card</title>
<link href="https://fonts.googleapis.com/css2?family=Questrial&family=Montserrat:wght@700&display=swap" rel="stylesheet">
<style>
  :root {
    --page: #ecebe6;
    --card: #fffdcb;
    --card-edge: #f5c9a2;
    --peach: #f7cfa8;
    --hot-pink: #ee1b8e;
    --white: #ffffff;
  }
  * { box-sizing: border-box; margin: 0; padding: 0; }
  html, body {
    width: 1200px;
    height: 1000px;
    overflow: hidden;
    background: var(--page);
  }
  .business-card {
    position: absolute;
    left: 150px;
    top: 230px;
    width: 900px;
    height: 540px;
    background: var(--card);
    border: 6px solid var(--card-edge);
    border-radius: 42px;
    overflow: hidden;
    font-family: "Questrial", sans-serif;
  }
  .brand {
    position: absolute;
    left: 250px;
    top: 60px;
    display: flex;
    align-items: center;
    gap: 34px;
  }
  .brand-dot {
    width: 140px;
    height: 140px;
    border-radius: 50%;
    background: var(--hot-pink);
  }
  .brand-name {
    font-size: 112px;
    line-height: 1;
    color: var(--peach);
    letter-spacing: 2px;
    margin-top: 60px;
  }
  .tagline {
    position: absolute;
    left: 0;
    right: 0;
    top: 262px;
    text-align: center;
    font-size: 31px;
    color: var(--hot-pink);
  }
  .holder-name {
    position: absolute;
    left: 0;
    right: 0;
    top: 340px;
    text-align: center;
    font-family: "Montserrat", sans-serif;
    font-weight: 700;
    font-size: 30px;
    color: var(--peach);
    letter-spacing: 1px;
  }
  .contact-band {
    position: absolute;
    left: 0;
    right: 0;
    top: 430px;
    height: 60px;
    background: var(--hot-pink);
    display: flex;
    align-items: center;
    justify-content: space-between;
    padding: 0 30px;
    color: var(--white);
    font-size: 27px;
  }
  .contact-item {
    display: flex;
    align-items: center;
    gap: 12px;
  }
  .contact-item svg { display: block; }
</style>
</head>
<body>
  <div class="business-card">
    <div class="brand">
      <div class="brand-dot"></div>
      <div class="brand-name">PLUM</div>
    </div>
    <p class="tagline">Coastal Society of Junior Equestrian Arts</p>
    <p class="holder-name">MARLENE TOBBITT</p>
    <div class="contact-band">
      <span class="contact-item">
        <svg width="16" height="26" viewBox="0 0 16 26" aria-hidden="true">
          <rect x="1.5" y="1.5" width="13" height="23" rx="2.5" fill="none" stroke="#fff" stroke-width="2"/>
          <line x1="5" y1="20.5" x2="11" y2="20.5" stroke="#fff" stroke-width="2"/>
        </svg>
        041 555 0186
      </span>
      <span class="contact-item">
        plum@mailbox.com
        <svg width="26" height="18" viewBox="0 0 26 18" aria-hidden="true">
          <rect x="1" y="1" width="24" height="16" fill="none" stroke="#fff" stroke-width="2"/>
          <polyline points="1,1 13,10 25,1" fill="none" stroke="#fff" stroke-width="2"/>
        </svg>
      </span>
    </div>
  </div>
</body>
</html>
```